ROLL-ON-VERANDA Business Card Design

Please do not submit more than one design per designer. Both the front and the back must be submitted as a single design. Please use all of the attached files to design a two-sided business card. Do not use tiny text that is hard to read. Do not put text or images too close to the edges where it might get cut off during printing. The card should be horizontal. Please do not send me the same design that I attached showing the business information. Be creative.

One file is marked as the primary logo for company. Other files are marked as secondary. All logos should be incorporated into the design with a focus on the primary one being bigger.

```html
<!DOCTYPE html>
<html lang="en">
<head>
<meta charset="utf-8">
<title>ROLL-ON-VERANDA Business Card</title>
<link rel="stylesheet" href="https://fonts.googleapis.com/css2?family=Roboto:ital,wght@0,400;0,700;1,400;1,700&family=Exo+2:ital,wght@1,900&display=swap">
<style>
  :root {
    --navy: #020b3e;
    --sea: #5a68c4;
    --sea-light: #7480d0;
    --white: #ffffff;
    --gold: #f5c330;
    --paper: #ffffff;
  }
  * { margin: 0; padding: 0; box-sizing: border-box; }
  html, body { width: 1200px; height: 1200px; overflow: hidden; background: var(--paper); }
  body { position: relative; font-family: "Roboto", Arial, sans-serif; }

  .card { position: absolute; overflow: hidden; box-shadow: 2px 4px 6px rgba(0,0,0,0.18); }
  .card-front { left: 113px; top: 31px; width: 981px; height: 561px; }
  .card-back  { left: 115px; top: 613px; width: 979px; height: 559px; }
  .card-shapes { position: absolute; inset: 0; width: 100%; height: 100%; }

  .contact-line {
    position: absolute; left: 39px; color: var(--white);
    font-size: 30px; font-weight: 400; line-height: 1; white-space: nowrap;
  }
  .tagline {
    position: absolute; left: 38px; top: 400px; color: var(--white);
    font-size: 25px; font-weight: 700; font-style: italic; line-height: 39px;
  }

  .boat-art {
    position: absolute; border-radius: 50% 50% 40% 40% / 60% 60% 40% 40%;
    background: radial-gradient(ellipse at center, #2a3470 0%, #121a55 55%, rgba(2,11,62,0) 80%);
  }
  .front-boat { left: 527px; top: 156px; width: 382px; height: 144px; }
  .back-boat  { left: 91px; top: 40px; width: 294px; height: 113px; }

  .wordmark {
    position: absolute; color: var(--white); font-weight: 700;
    line-height: 1; white-space: nowrap; text-align: center;
  }
  .front-wordmark { left: 499px; top: 305px; width: 420px; font-size: 40px; }
  .back-wordmark  { left: 73px; top: 160px; width: 320px; font-size: 31px; }

  .captain-name {
    position: absolute; left: 72px; top: 262px; color: var(--white);
    font-family: "Exo 2", "Roboto", sans-serif; font-weight: 900; font-style: italic;
    font-size: 44px; letter-spacing: 2px; line-height: 1; white-space: nowrap;
  }
  .credential {
    position: absolute; left: 66px; color: var(--gold);
    font-size: 30px; font-style: italic; font-weight: 400; line-height: 1; white-space: nowrap;
  }
</style>
</head>
<body>

<section class="card card-front">
  <svg class="card-shapes" viewBox="0 0 1570 897" preserveAspectRatio="none">
    <defs>
      <linearGradient id="sea-front" x1="0" y1="0" x2="1" y2="1">
        <stop offset="0" stop-color="var(--sea-light)"/>
        <stop offset="0.5" stop-color="var(--sea)"/>
        <stop offset="1" stop-color="var(--sea-light)"/>
      </linearGradient>
    </defs>
    <rect width="1570" height="897" fill="url(#sea-front)" role="img" aria-label="Rippling pool water light pattern"/>
    <path fill="var(--navy)" d="M0,277 H705 C760,150 880,20 1060,0 H1570 V897 H1060 C880,880 760,750 694,587 H0 Z"/>
  </svg>

  <div class="contact-line" style="top:193px">www.Roll-On-Veranda.com</div>
  <div class="contact-line" style="top:243px">service@rollonveranda.com</div>
  <div class="contact-line" style="top:293px">TEXT (555) 014 - 2290</div>

  <p class="tagline">Providing hands-on boat training,<br>Captaining services and deliveiries<br>in the Bayview County area.</p>

  <div class="boat-art front-boat" role="img" aria-label="Illustration of a cabin motorboat on the water"></div>
  <div class="wordmark front-wordmark">ROLL-ON-VERANDA</div>
</section>

<section class="card card-back">
  <svg class="card-shapes" viewBox="0 0 1567 894" preserveAspectRatio="none">
    <defs>
      <linearGradient id="sea-back" x1="0" y1="0" x2="1" y2="1">
        <stop offset="0" stop-color="var(--sea-light)"/>
        <stop offset="0.5" stop-color="var(--sea)"/>
        <stop offset="1" stop-color="var(--sea-light)"/>
      </linearGradient>
    </defs>
    <rect width="1567" height="894" fill="url(#sea-back)" role="img" aria-label="Rippling pool water light pattern"/>
    <path fill="var(--navy)" d="M0,0 H496 C700,10 820,160 866,292 H1567 V601 H866 C820,760 680,880 496,894 H0 Z"/>
    <g class="partner-badges">
      <circle cx="901" cy="779" r="70" fill="var(--white)" stroke="var(--gold)" stroke-width="6"/>
      <circle cx="901" cy="779" r="52" fill="#111111"/>
      <circle cx="1081" cy="779" r="72" fill="#0f1a5c"/>
      <circle cx="1081" cy="779" r="44" fill="#c8102e"/>
      <circle cx="1271" cy="779" r="72" fill="var(--white)" stroke="#c8102e" stroke-width="6"/>
      <circle cx="1271" cy="779" r="44" fill="#2a3a8c"/>
      <circle cx="1456" cy="779" r="66" fill="var(--white)" stroke="#1f5fa8" stroke-width="8"/>
      <circle cx="1456" cy="779" r="40" fill="#1f3f8a"/>
    </g>
  </svg>

  <div class="boat-art back-boat" role="img" aria-label="Illustration of a cabin motorboat on the water"></div>
  <div class="wordmark back-wordmark">ROLL-ON-VERANDA</div>

  <h1 class="captain-name">CAPTAIN DANA R. HOLLOWAY</h1>

  <div class="credential" style="top:330px">USCG Licensed Master Captain</div>
  <div class="credential" style="top:380px">NMSA Certified Instructor</div>
  <div class="credential" style="top:430px">Graduate Degree</div>
  <div class="credential" style="top:480px">Veteran</div>
</section>

</body>
</html>
```